REALTOR/REALESTATE INVESTOR CARD

I AM MY LOCAL CITIES FLIP THIS HOUSE KING...I CHANGE NEIGHBORHOODS ONE HOUSE AT A TIME. I BUY OLD HOUSES FOR CASH TOTALLY RENOVATE THEM TO LIKE NEW, THEN RE SELL THEM...
I HAVE BEEN USING PLATINUM & BURGANDY AS MY MAIN COLOR..
I WANT SOMETHING FUN AND MODERN TO APPEAL TO ALL BUYERS AND SELLERS. AND TO REFLECT I AM AT THE TOP OF MY GAME...A WOW...THIS IS A GREAT CARD.......WOW.......I AM A REALTOR....I FLIP HOUSES.....MAYBE SHOW AND OLD HOUSE AND THEN A SPARKLING NEW HOUSE..... MY COMPANY NAME IS HOMESTEAD CAPITAL PARTNERS THE ADDRESS IS P.O.BOX 86 GOOSE CREEK, S.C. 29401

Target Market(s)

I SELL HOUSES THAT HAVE BEEN RENOVATED TO ALMOST BRAND NEW CONDITION.......I ALSO BUY HOUSES/MOBILES FOR ALL CASH FAST CLOSINGS..
I BUY GOOSE CREEK HOUSES ALL CASH FAST CLOSE.....I BUY MOBILE HOMES ANY CONDITION, ANY PRICE.....Buyers & sellers of houses.....

Industry/Entity Type

Investment

Font styles to use
Sans Serif

Requirements
Must have
• I BUY GOOSE CREEK HOUSES ALL CASH FAST CLOSINGS......
CHANGING GOOSE CREEK, ONE HOUSE AT A TIME...
RAY T. BELLAMY CIAS
REALTOR/CERTIFIED INVESTOR AGENT
HOMESTEAD CAPITAL PARTNERS,LLC.
P.O. BOX 86
GOOSE CREEK, S.C. 29401
843-555-0172
RAYBELLAMYHOUSES@QUILLMAIL.EXAMPLE
Nice to have
• GOOSE CREEK'S RE-HAB KING....
A actual picture of MAYBE A HOME BEING RENOVATED
TO ONE LOOKING AWESOME.....artwork
Should not have
• a picture of and old ugly home the a sparkling brand new one that is what I di I renovate homes.......

```html
<!DOCTYPE html>
<html lang="en">
<head>
<meta charset="utf-8">
<title>Homestead Capital Partners – Business Card</title>
<link href="https://fonts.googleapis.com/css2?family=Arimo:wght@400;700&family=Tinos:wght@400;700&display=swap" rel="stylesheet">
<style>
  :root {
    --page-bg: #d9d7d3;
    --burgundy: #a3252b;
    --burgundy-deep: #8c1d22;
    --platinum: #6f6f72;
    --white: #ffffff;
    --ink: #111111;
    --card-edge: #f4f4f4;
  }
  * { margin: 0; padding: 0; box-sizing: border-box; }
  html, body {
    width: 1200px; height: 768px; overflow: hidden;
    background: var(--page-bg);
    font-family: "Arimo", Arial, sans-serif;
  }
  .canvas { position: relative; width: 1200px; height: 768px; }

  .card {
    position: absolute; top: 229px; width: 540px; height: 310px;
    overflow: hidden;
    box-shadow: 0 6px 18px rgba(0,0,0,0.25);
  }

  /* ---------- Front ---------- */
  .card-front { left: 45px; background: var(--burgundy); border: 4px solid var(--card-edge); }
  .company-name {
    position: absolute; left: 36px; top: 22px;
    color: var(--white); font-size: 19px; line-height: 1.12; letter-spacing: 0.5px;
  }
  .renovation-art {
    position: absolute; left: 16px; top: 132px; width: 178px; height: 118px;
    border-radius: 40% 45% 30% 35% / 45% 40% 30% 30%;
    background: radial-gradient(ellipse at 50% 30%, #dfe6f1 0%, #9fb6c9 40%, #6b8a57 75%, #4f6e3c 100%);
  }
  .renovation-caption {
    position: absolute; left: 38px; top: 256px;
    color: var(--white); font-size: 10px; line-height: 1.2; letter-spacing: 0.3px;
  }
  .feature-frame-shadow {
    position: absolute; left: 200px; top: 38px; width: 326px; height: 256px;
    background: var(--ink);
  }
  .feature-frame {
    position: absolute; left: 210px; top: 48px; width: 302px; height: 222px;
    background: var(--white); border: 2px solid #cfcfcf;
  }
  .feature-tagline {
    position: absolute; left: 8px; top: 8px;
    color: var(--burgundy); font-size: 11px; font-weight: 700; letter-spacing: 0.2px;
  }
  .finished-home-art {
    position: absolute; left: 22px; top: 30px; width: 258px; height: 180px;
    background: linear-gradient(180deg, #cfe0f2 0%, #a9c3da 35%, #5f7c95 55%, #6f9a4c 80%, #4d7a32 100%);
    border-radius: 6px;
  }

  /* ---------- Back ---------- */
  .card-back { left: 615px; background: var(--platinum); border: 4px solid var(--card-edge); }
  .rehab-title {
    position: absolute; left: 232px; top: 30px;
    color: var(--white); font-size: 9px; letter-spacing: 0.4px;
  }
  .agent-name {
    position: absolute; left: 232px; top: 44px;
    font-family: "Tinos", "Times New Roman", serif;
    color: var(--burgundy); font-size: 22px; letter-spacing: 1px;
  }
  .agent-role {
    position: absolute; left: 232px; top: 74px;
    color: var(--white); font-size: 10px; letter-spacing: 0.3px;
  }
  .rule-white { position: absolute; left: 220px; right: 0; top: 92px; height: 3px; background: var(--white); }
  .rule-thin-red { position: absolute; left: 240px; right: 0; top: 98px; height: 2px; background: var(--burgundy); }
  .offer-band {
    position: absolute; left: 0; right: 0; top: 140px; height: 20px;
    background: var(--burgundy); border-top: 3px solid var(--white);
  }
  .offer-text {
    position: absolute; left: 36px; top: 2px;
    color: var(--white); font-size: 11px; font-weight: 700; letter-spacing: 0.3px;
  }
  .contact-bar { position: absolute; left: 0; width: 38px; top: 204px; height: 8px; background: var(--burgundy); }
  .contact-label {
    position: absolute; left: 44px; top: 200px;
    color: var(--burgundy); font-size: 11px; font-weight: 700;
  }
  .contact-bar-right { position: absolute; left: 130px; right: 0; top: 204px; height: 3px; background: var(--burgundy); }
  .contact-details {
    position: absolute; left: 44px; top: 216px;
    color: var(--white); font-size: 12px; line-height: 1.3; font-style: normal;
  }
  .email-band {
    position: absolute; left: 0; right: 0; top: 262px; height: 30px;
    background: var(--burgundy-deep);
  }
  .email-text {
    position: absolute; left: 44px; top: 1px;
    color: var(--white); font-size: 12px;
  }
</style>
</head>
<body>
<main class="canvas">

  <section class="card card-front" aria-label="Card front">
    <h1 class="company-name">HOMESTEAD<br>CAPITAL<br>PARTNERS,LLC.</h1>
    <div class="renovation-art" role="img" aria-label="Illustration of a two-storey home mid-renovation among trees"></div>
    <p class="renovation-caption">A HOME BEING RENOVATED<br>TO ONE LOOKING AWESOME...</p>
    <div class="feature-frame-shadow"></div>
    <div class="feature-frame">
      <p class="feature-tagline">CHANGING GOOSE CREEK,ONE HOUSE AT A TIME.....</p>
      <div class="finished-home-art" role="img" aria-label="Illustration of a fully renovated two-storey blue house with garage and green lawn"></div>
    </div>
  </section>

  <section class="card card-back" aria-label="Card back">
    <p class="rehab-title">THE GOOSE CREEK'S RE-HAB KING....</p>
    <h2 class="agent-name">RAY T. BELLAMY CIAS</h2>
    <p class="agent-role">REALTOR/CERTIFIED INVESTOR AGENT</p>
    <div class="rule-white"></div>
    <div class="rule-thin-red"></div>
    <div class="offer-band"><p class="offer-text">I BUY GOOSE CREEK HOUSES ALL CASH FAST CLOSINGS.....</p></div>
    <div class="contact-bar"></div>
    <p class="contact-label">CONTACT ME</p>
    <div class="contact-bar-right"></div>
    <address class="contact-details">
      P.O. BOX 86<br>
      GOOSE CREEK, S.C. 29401<br>
      843-555-0172
    </address>
    <div class="email-band"><p class="email-text">raybellamyhouses@quillmail.example</p></div>
  </section>

</main>
</body>
</html>
```